Bookmarks for teachers and high school students - Range of 6

We are after a range of 6 bookmarks to use as hand outs to schools and students that we supply books and other school resources to.

Each bookmark is to have an inspirational quote on it and be a different color. You can decide color and background texture.

The back of them shall all be black or white, so just fronts needed. We want these 6 bookmarks to be similar in design, so they look like a matching range. And be nice enough that teachers and students will pick one to use.

We also want our logo to be on the bookmark, maybe just tucked down the bottom and our web address showing please - www.tarleby.com.au

Attached is the 6 quotes we want to use and an examples of the type of font I would like to see. But each a different font ..Also attached is our logo.

I think simple and smart may be best, but see what you come up with as I am also open to making them funky for students (if possible)

The print size of each bookmark is 40mm by 210mm

Target Market(s)

teachers and high school students

Industry/Entity Type

School

Requirements
Must have
• be eye catching

```html
<!DOCTYPE html>
<html lang="en">
<head>
<meta charset="utf-8">
<title>Tarleby Bookmark Range</title>
<link rel="stylesheet" href="https://fonts.googleapis.com/css2?family=Cinzel:wght@400;700&family=Oswald:wght@400;600&family=Lobster&family=Open+Sans:wdth,wght@75,300;75,700&family=Playfair+Display&family=Montserrat:wght@400;600&display=swap">
<style>
:root{
  --canvas:#efe9e1;
  --ink-white:#ffffff;
  --night-top:#1b2a3a; --night-bottom:#070b10; --night-text:#57bde6; --night-logo:#6f6f70; --night-url:#2a2a2a;
  --pink-top:#e2157f; --pink-bottom:#8a1d6b; --pink-logo:#f47fbc; --pink-url:#e5157f;
  --violet-top:#8e72c4; --violet-bottom:#3b2a7d; --violet-logo:#a98dcc; --violet-url:#5c3f91;
  --leaf-top:#9ad48c; --leaf-bottom:#4f8a2c; --leaf-logo:#9fd391; --leaf-url:#2c6a30; --leaf-band:#e8f0b8;
  --ocean-top:#2a9bd0; --ocean-bottom:#0f3550; --ocean-logo:#40667f; --ocean-url:#153a52;
  --amber-top:#e86a18; --amber-bottom:#f59a2a; --amber-text:#ffd43a; --amber-logo:#f5a75e; --amber-url:#e27a1f;
  --logo-text:#3a3a3a;
}
*{margin:0;padding:0;box-sizing:border-box}
html,body{width:1200px;height:729px;overflow:hidden;background:var(--canvas)}
.range{position:relative;width:1200px;height:729px}
.bookmark{position:absolute;top:47px;width:117px;height:613px;overflow:hidden;box-shadow:0 4px 12px rgba(0,0,0,.35)}
.bookmark__art{position:absolute;inset:0 0 92px 0}
.bookmark__quote{position:absolute;top:16px;left:5px;right:5px;text-align:center;color:var(--ink-white);line-height:1.05}
.bookmark__quote span{display:block}
.bookmark__credit{position:absolute;bottom:98px;left:0;right:0;text-align:center;font:10px 'Playfair Display',serif;color:var(--ink-white);line-height:1.15}
.bookmark__logo{position:absolute;bottom:28px;left:0;right:0;height:64px;display:flex;align-items:center;justify-content:center}
.bookmark__logo-name{font:600 15px 'Montserrat',sans-serif;letter-spacing:1px;color:var(--logo-text)}
.bookmark__url{position:absolute;bottom:0;left:0;right:0;height:28px;display:flex;align-items:center;justify-content:center;font:600 8.5px 'Montserrat',sans-serif;color:var(--ink-white)}
.ribbon{background:var(--ink-white);margin:4px 0;padding:3px 0;clip-path:polygon(0 0,100% 0,94% 50%,100% 100%,0 100%,6% 50%)}

.bm-night{left:163px}
.bm-night .bookmark__art{background:linear-gradient(180deg,var(--night-top),#0d1a28 55%,var(--night-bottom))}
.bm-night .bookmark__quote{font-family:'Cinzel',serif;color:var(--night-text);line-height:1}
.bm-night .bookmark__logo{background:var(--night-logo)}
.bm-night .bookmark__url{background:var(--night-url)}
.rule{height:1px;background:var(--night-text);margin:10px 8px 12px;opacity:.7}

.bm-pink{left:313px}
.bm-pink .bookmark__art{background:linear-gradient(180deg,var(--pink-top),#c3187c 50%,var(--pink-bottom))}
.bm-pink .bookmark__logo{background:var(--pink-logo)}
.bm-pink .bookmark__url{background:var(--pink-url)}

.bm-violet{left:464px}
.bm-violet .bookmark__art{background:linear-gradient(180deg,var(--violet-top),#6a4fb0 50%,var(--violet-bottom))}
.bm-violet .bookmark__logo{background:var(--violet-logo)}
.bm-violet .bookmark__url{background:var(--violet-url)}

.bm-leaf{left:618px}
.bm-leaf .bookmark__art{background:linear-gradient(180deg,var(--leaf-top) 0,var(--leaf-top) 48%,#7fb85a 70%,var(--leaf-bottom))}
.bm-leaf .bookmark__quote{font-family:'Open Sans',sans-serif;font-stretch:75%;font-weight:300}
.bm-leaf .bookmark__logo{background:var(--leaf-logo)}
.bm-leaf .bookmark__url{background:var(--leaf-url)}
.leaf-band{background:var(--leaf-band);color:#2c3a1e;margin:3px -5px;padding:2px 0}

.bm-ocean{left:768px}
.bm-ocean .bookmark__art{background:linear-gradient(180deg,var(--ocean-top),#1c6e9c 55%,var(--ocean-bottom))}
.bm-ocean .bookmark__logo{background:var(--ocean-logo)}
.bm-ocean .bookmark__logo-name{color:#e6eef3}
.bm-ocean .bookmark__url{background:var(--ocean-url)}
.bm-ocean .ribbon{color:var(--ocean-top);margin:4px 6px}

.bm-amber{left:919px}
.bm-amber .bookmark__art{background:linear-gradient(180deg,var(--amber-top),#f07d1e 50%,var(--amber-bottom))}
.bm-amber .bookmark__quote{color:var(--amber-text)}
.bm-amber .bookmark__logo{background:var(--amber-logo)}
.bm-amber .bookmark__url{background:var(--amber-url)}

.f-script{font-family:'Lobster',cursive}
.f-cond{font-family:'Oswald',sans-serif}
.f-cond-b{font-family:'Oswald',sans-serif;font-weight:600}
.f-serif{font-family:'Playfair Display',serif}
</style>
</head>
<body>
<main class="range">

  <article class="bookmark bm-night">
    <div class="bookmark__art" role="img" aria-label="Dark blue smoky texture with glowing embers"></div>
    <p class="bookmark__quote">
      <span style="font-size:16px">&ldquo;It doesn't</span>
      <span style="font-size:15px">matter</span>
      <span style="font-size:34px;margin-top:4px">Who</span>
      <span style="font-size:27px">we are</span>
      <span class="rule"></span>
      <span style="font-size:17px">What</span>
      <span style="font-size:17px">matters</span>
      <span style="font-size:29px;margin-top:2px">is our</span>
      <span style="font-size:29px">plan&rdquo;</span>
    </p>
    <p class="bookmark__credit">The Night<br>Harbour</p>
    <div class="bookmark__logo"><span class="bookmark__logo-name">TARLEBY</span></div>
    <div class="bookmark__url">www.tarleby.com.au</div>
  </article>

  <article class="bookmark bm-pink">
    <div class="bookmark__art" role="img" aria-label="Magenta grunge paint texture"></div>
    <p class="bookmark__quote" style="top:20px">
      <span class="f-script" style="font-size:19px">All our</span>
      <span class="f-cond-b" style="font-size:26px">DREAMS</span>
      <span class="f-script" style="font-size:14px;margin-top:2px">can come true</span>
      <span class="ribbon f-cond" style="font-size:13px;color:var(--pink-top);margin:6px -2px">IF WE HAVE THE</span>
      <span class="f-cond-b" style="font-size:29px;letter-spacing:-.5px">COURAGE</span>
      <span class="f-cond" style="font-size:17px;margin-top:3px"><em class="f-script" style="font-style:normal">to</em> PURSUE</span>
      <span class="f-cond" style="font-size:16px">THEM</span>
    </p>
    <p class="bookmark__credit">Wendell Darcy</p>
    <div class="bookmark__logo"><span class="bookmark__logo-name">TARLEBY</span></div>
    <div class="bookmark__url">www.tarleby.com.au</div>
  </article>

  <article class="bookmark bm-violet">
    <div class="bookmark__art" role="img" aria-label="Violet glow with flowing light streaks"></div>
    <p class="bookmark__quote">
      <span class="f-script" style="font-size:16px">&ldquo;Those that</span>
      <span class="f-cond" style="font-size:17px;margin-top:5px">DON'T BELIEVE</span>
      <span class="f-cond" style="font-size:16px">IN</span>
      <span class="f-cond-b" style="font-size:40px;margin-top:4px">MAGIC</span>
      <span class="f-script" style="font-size:22px;margin-top:2px">will never</span>
      <span class="f-cond-b" style="font-size:42px;margin-top:4px">FIND</span>
      <span class="f-cond-b" style="font-size:42px">IT&rdquo;</span>
    </p>
    <p class="bookmark__credit">Rowan Dale</p>
    <div class="bookmark__logo"><span class="bookmark__logo-name">TARLEBY</span></div>
    <div class="bookmark__url">www.tarleby.com.au</div>
  </article>

  <article class="bookmark bm-leaf">
    <div class="bookmark__art" role="img" aria-label="Soft green backdrop with cupped hands holding a young tree"></div>
    <p class="bookmark__quote">
      <span style="font-size:20px">&ldquo;The best</span>
      <span style="font-size:20px">time to plant</span>
      <span class="f-cond-b" style="font-size:32px;margin-top:2px">A TREE</span>
      <span style="font-size:13px;font-weight:700">was 20 years ago</span>
      <span style="font-size:18px;margin-top:6px">The second</span>
      <span class="leaf-band" style="font-size:20px;font-weight:700">best time</span>
      <span style="font-size:20px">is <b style="font-weight:700">NOW</b>&rdquo;</span>
    </p>
    <p class="bookmark__credit">Chinese Proverb</p>
    <div class="bookmark__logo"><span class="bookmark__logo-name">TARLEBY</span></div>
    <div class="bookmark__url">www.tarleby.com.au</div>
  </article>

  <article class="bookmark bm-ocean">
    <div class="bookmark__art" role="img" aria-label="Blue misty light over water"></div>
    <p class="bookmark__quote">
      <span class="f-serif" style="font-size:24px">&ldquo;Logic</span>
      <span class="ribbon f-script" style="font-size:15px">will get</span>
      <span class="f-script" style="font-size:13px">you</span>
      <span class="f-serif" style="font-size:16px;margin-top:4px">from A to Z</span>
      <span class="f-cond" style="font-size:21px;margin-top:6px">IMAGINATION</span>
      <span class="ribbon f-script" style="font-size:15px">will get</span>
      <span class="f-script" style="font-size:13px">you</span>
      <span class="f-script" style="font-size:17px;margin-top:2px">everywhere&rdquo;</span>
    </p>
    <p class="bookmark__credit">Alden Eastwood</p>
    <div class="bookmark__logo"><span class="bookmark__logo-name">TARLEBY</span></div>
    <div class="bookmark__url">www.tarleby.com.au</div>
  </article>

  <article class="bookmark bm-amber">
    <div class="bookmark__art" role="img" aria-label="Warm orange glow with joined hands"></div>
    <p class="bookmark__quote">
      <span class="f-script" style="font-size:20px">&ldquo;Coming</span>
      <span class="f-cond" style="font-size:20px">TOGETHER IS</span>
      <span class="f-cond" style="font-size:18px">A BEGINNING;</span>
      <span class="f-script" style="font-size:20px;margin-top:6px">Keeping</span>
      <span class="f-cond" style="font-size:20px">TOGETHER IS</span>
      <span class="f-cond" style="font-size:18px">PROGRESS;</span>
      <span class="f-script" style="font-size:20px;margin-top:6px">Working</span>
      <span class="f-cond" style="font-size:20px">TOGETHER IS</span>
      <span class="f-cond" style="font-size:18px">SUCCESS</span>
    </p>
    <p class="bookmark__credit">Harlan Foster</p>
    <div class="bookmark__logo"><span class="bookmark__logo-name">TARLEBY</span></div>
    <div class="bookmark__url">www.tarleby.com.au</div>
  </article>

</main>
</body>
</html>
```